Business card for communications

Need a business card for my consulting business - I work with not for profits, start ups and social enterprises on their media, communications campaigns.

Please see my website for colours, images and fonts www.morvenquillet.example

Morven Quillet
Communications & Campaign strategist
Sydney - Melbourne
M: 0498 317 250
E: morven@morvenquillet.example
S: morvenquillet
W: morvenquillet.example
T: @morvenquillet

(above is info only and can be presented any way e.g. should not have to be M for mobile - it should be an icon)
Updates

Dear designers I have updated the brief and uploaded high res images from my website for you to use. The designs so far with the use of images and icons are much better so far. Thank you I look forward to receiving your revised designs. Morven Quillet

Industry/Entity Type

Communications

Font styles to use
Sans Serif

Requirements
Must have
• Icons for contact details
Images from the website www.morvenquillet.example
Nice to have
• Images - attached

```html
<!DOCTYPE html>
<html lang="en">
<head>
<meta charset="utf-8">
<title>Morven Quillet – Business Card</title>
<link href="https://fonts.googleapis.com/css2?family=Questrial&family=Noto+Sans:wght@700&display=swap" rel="stylesheet">
<style>
  :root {
    --ink: #000000;
    --card-black: #0b0b0b;
    --accent: #f7d117;
    --paper: #ffffff;
    --silver-light: #ffffff;
    --silver-dark: #a9a9a9;
    --social: #2aa6e0;
    --name-dark: #161616;
  }
  * { margin: 0; padding: 0; box-sizing: border-box; }
  html, body {
    width: 1200px; height: 600px; overflow: hidden;
    background: var(--paper);
  }
  .canvas {
    position: relative; width: 1200px; height: 600px;
  }
  .card {
    position: absolute; top: 140px; width: 540px; height: 320px;
    border-radius: 0 120px 0 120px; overflow: hidden;
  }
  /* Front */
  .card-front {
    left: 40px; background: var(--card-black);
    font-family: "Questrial", sans-serif; color: var(--paper);
  }
  .brand {
    position: absolute; left: 30px; top: 112px; width: 210px;
    display: flex; align-items: center; gap: 10px;
  }
  .brand-mark {
    width: 14px; height: 14px; background: var(--accent); flex: none;
  }
  .brand-name {
    color: var(--accent); font-size: 30px; line-height: 1.05;
  }
  .divider {
    position: absolute; left: 258px; top: 82px; width: 3px; height: 200px;
    background: var(--accent);
  }
  .details {
    position: absolute; left: 278px; top: 100px; right: 10px;
  }
  .details .name {
    color: var(--accent); font-size: 25px; margin-left: 4px; line-height: 1.1;
  }
  .details .role { font-size: 10.5px; margin-top: 5px; }
  .details .region { font-size: 14px; margin-top: 1px; }
  .contact-list { list-style: none; margin-top: 6px; }
  .contact-list li {
    display: flex; align-items: center; gap: 12px;
    font-size: 14px; height: 24px;
  }
  .contact-list svg { width: 16px; height: 14px; flex: none; }
  .social-row { display: flex; gap: 26px; margin-top: 10px; font-size: 14px; }
  .social-row span { display: flex; align-items: center; gap: 6px; }
  .social-dot {
    width: 15px; height: 15px; border-radius: 3px; background: var(--social);
  }
  /* Back */
  .card-back {
    left: 620px;
    background: radial-gradient(ellipse at 50% 48%, var(--silver-light) 0%, #e6e6e6 40%, var(--silver-dark) 100%);
  }
  .card-back .corners { position: absolute; inset: 0; width: 100%; height: 100%; }
  .back-name {
    position: absolute; left: 0; right: 0; top: 128px; text-align: center;
    font-family: "Noto Sans", sans-serif; font-weight: 700; font-size: 46px;
    color: var(--name-dark);
    text-shadow: 2px 3px 3px rgba(0,0,0,0.45);
  }
</style>
</head>
<body>
<main class="canvas">
  <section class="card card-front" aria-label="Card front">
    <div class="brand">
      <span class="brand-mark"></span>
      <span class="brand-name">Morven<br>Quillet</span>
    </div>
    <div class="divider"></div>
    <div class="details">
      <p class="name">Morven Quillet</p>
      <p class="role">Communications &amp; Campaign strategist</p>
      <p class="region">Sydney - Melbourne</p>
      <ul class="contact-list">
        <li>
          <svg viewBox="0 0 16 14" aria-hidden="true"><path fill="#f7d117" d="M1 4c0-2 3-3 7-3s7 1 7 3v1h-4V3.5H5V5H1zM3 6h10l2 7H1z"/><circle cx="8" cy="9.5" r="2" fill="#0b0b0b"/></svg>
          0498 317 250
        </li>
        <li>
          <svg viewBox="0 0 16 14" aria-hidden="true"><rect x="0.5" y="2" width="15" height="10" fill="#f7d117"/><path d="M0.5 2l7.5 6 7.5-6" fill="none" stroke="#0b0b0b" stroke-width="1.2"/></svg>
          morven@morvenquillet.example
        </li>
        <li>
          <svg viewBox="0 0 16 14" aria-hidden="true"><g fill="none" stroke="#f7d117" stroke-width="1.2"><circle cx="8" cy="7" r="6"/><ellipse cx="8" cy="7" rx="2.6" ry="6"/><path d="M2 7h12M3 4h10M3 10h10"/></g></svg>
          morvenquillet.example
        </li>
      </ul>
      <div class="social-row">
        <span><i class="social-dot"></i>morvenquillet</span>
        <span><i class="social-dot"></i>@morvenquillet</span>
      </div>
    </div>
  </section>

  <section class="card card-back" aria-label="Card back">
    <svg class="corners" viewBox="0 0 540 320" preserveAspectRatio="none" aria-hidden="true">
      <polygon points="330,0 540,0 540,70" fill="#f7d117"/>
      <polygon points="540,130 540,320 500,320" fill="#f7d117"/>
      <polygon points="0,0 30,0 0,120" fill="#f7d117"/>
      <polygon points="0,240 0,320 230,320" fill="#f7d117"/>
    </svg>
    <p class="back-name">Morven Quillet</p>
  </section>
</main>
</body>
</html>
```